Flyer to Promote Membership in a Trade Association

UPDATE: I am looking for something modern and clean. NO CLIP ART. Not flashy. Just professional and modern. For everyone looking at our current flyer, we don't like it. That's why we aer looking for a new one. So please don't replicate it or use it as inspiration.

I need a flyer to promote membership in the Durable Residence Backers League. It can (probably should) be 2-sided. The content is attached as well as our logo and brand guidelines.

```html
<!DOCTYPE html>
<html lang="en">
<head>
<meta charset="utf-8">
<title>DRBL Membership Flyer</title>
<link rel="stylesheet" href="https://fonts.googleapis.com/css2?family=Montserrat:wght@500;600;700;800&family=Open+Sans:wght@400;600;700&display=swap">
<style>
:root{
  --orange:#ee7a2a;
  --orange-dark:#d8651a;
  --slate:#4d5358;
  --slate-dark:#3a3f44;
  --slate-light:#6b7177;
  --mist:#e4e6e8;
  --paper:#ffffff;
  --ink:#2f3337;
  --stage:#ececec;
}
*{box-sizing:border-box;margin:0;padding:0}
html,body{width:1200px;height:3000px;overflow:hidden}
body{background:var(--stage);font-family:"Open Sans",Arial,sans-serif;color:var(--ink);position:relative}
.page{position:absolute;left:100px;width:1000px;height:1294px;background:var(--paper);overflow:hidden;box-shadow:0 2px 10px rgba(0,0,0,.08)}
.page--front{top:120px}
.page--back{top:1586px}
.abs{position:absolute}
.backdrop{position:absolute;left:0;top:0}

.brand{position:absolute;left:50px;top:44px;display:flex;align-items:center;gap:12px;z-index:3}
.brand__mark{width:34px;height:34px;background:var(--orange)}
.brand__name{font-family:"Montserrat",Arial,sans-serif;font-weight:700;font-size:15px;color:var(--slate);line-height:1.2;width:190px}

.photo{position:absolute;border-radius:50%;background:radial-gradient(circle at 45% 40%,#8d8a83 0%,#5e5c58 45%,#2f2e2c 100%);z-index:2}

.headline{position:absolute;left:50px;top:360px;z-index:3;color:#fff}
.headline__lead{font-family:"Montserrat",Arial,sans-serif;font-weight:800;font-size:66px;line-height:1}
.headline__tag{display:inline-block;margin-top:12px;background:var(--orange);font-family:"Montserrat",Arial,sans-serif;font-weight:600;font-size:26px;padding:6px 16px}
.headline__sub{margin-top:12px;font-family:"Montserrat",Arial,sans-serif;font-weight:600;font-size:22px;line-height:1.3;width:460px}
.intro{position:absolute;left:50px;top:590px;width:440px;color:#fff;font-size:13.5px;line-height:1.55;z-index:3}
.intro strong{color:var(--orange)}

.stats{position:absolute;left:50px;top:770px;z-index:3}
.stat{font-family:"Montserrat",Arial,sans-serif;font-weight:700;font-size:22px;color:var(--slate-dark);margin-bottom:10px;letter-spacing:.5px}
.stat b{color:var(--orange)}

.activities{position:absolute;left:570px;top:730px;width:380px;z-index:3;background:#fff;border:1px solid #cfd3d6}
.activities__title{background:var(--orange);color:#fff;font-family:"Montserrat",Arial,sans-serif;font-weight:700;font-size:24px;padding:10px 18px}
.activities ul{list-style:none;padding:14px 18px 16px}
.activities li{font-size:15px;line-height:1.75;color:var(--slate-dark)}
.activities li b{font-weight:700}

.access{position:absolute;left:470px;top:975px;width:480px;text-align:right;color:var(--orange);font-family:"Montserrat",Arial,sans-serif;font-weight:600;font-size:16px;line-height:1.4}

.join{position:absolute;left:50px;top:1030px;width:900px}
.join__tab{display:inline-block;background:var(--slate-dark);color:#fff;font-family:"Montserrat",Arial,sans-serif;font-weight:700;font-size:16px;padding:8px 18px}
.join__grid{display:grid;grid-template-columns:1fr 1fr;gap:14px;margin-top:10px}
.tier{background:var(--mist);padding:14px 18px;font-size:14px;line-height:1.55;color:var(--ink)}
.tier__name{font-family:"Montserrat",Arial,sans-serif;font-weight:700;font-size:16px;color:var(--slate-dark)}
.tier__price{color:var(--orange-dark);font-weight:700}

.footer{position:absolute;left:0;bottom:0;width:1000px;height:70px;background:var(--slate);display:flex;justify-content:space-between;align-items:center;padding:0 50px;font-family:"Montserrat",Arial,sans-serif;font-weight:600;font-size:20px}
.footer__cta{color:#fff}
.footer__url{color:var(--orange)}

/* back */
.benefits-panel{position:absolute;left:40px;top:150px;width:920px;height:560px;background:var(--mist);border-radius:22px}
.benefits-hero{position:absolute;left:40px;top:250px;width:420px;height:330px;background:var(--orange);border-radius:0 160px 160px 0;display:flex;align-items:center;padding-left:50px}
.benefits-hero h1{font-family:"Montserrat",Arial,sans-serif;font-weight:800;font-size:72px;line-height:1.02;color:#fff}
.feature-panel{position:absolute;left:490px;top:180px;width:450px;height:500px;background:var(--slate);border-radius:18px;padding:34px 34px;color:#fff}
.feature{margin-bottom:40px}
.feature h2{font-family:"Montserrat",Arial,sans-serif;font-weight:700;font-size:25px;line-height:1.2;margin-bottom:10px}
.feature h2::before{content:"";display:block;width:48px;height:5px;background:var(--orange);margin-bottom:12px}
.feature p{font-size:14.5px;line-height:1.55;color:#eceff1}

.perks{position:absolute;left:50px;top:760px;width:430px}
.perk{padding-left:20px;position:relative;margin-bottom:20px}
.perk::before{content:"";position:absolute;left:0;top:6px;width:9px;height:9px;background:var(--orange)}
.perk h3{font-family:"Montserrat",Arial,sans-serif;font-weight:700;font-size:17px;color:var(--slate-dark);margin-bottom:4px}
.perk h3 span{color:var(--orange);font-size:13px}
.perk p{font-size:13.5px;line-height:1.5}

.side-card{position:absolute;left:520px;top:750px;width:430px;border-left:5px solid var(--orange);padding:6px 0 6px 24px}
.side-card .perk{padding-left:0}
.side-card .perk::before{display:none}
.side-card .perk h3{font-size:19px}

.firms{position:absolute;left:40px;top:1030px;width:920px;background:var(--mist);padding:18px 26px;font-size:12.5px;line-height:1.65;color:var(--slate-dark);border-radius:8px}
</style>
</head>
<body>

<section class="page page--front">
  <svg class="backdrop" width="1000" height="1294" viewBox="0 0 1000 1294" aria-hidden="true">
    <path d="M0 320 L420 320 C520 320 560 380 600 470 C640 560 720 620 820 640 C900 655 960 650 1000 640 L1000 720 C880 740 760 760 620 750 C420 735 200 740 0 760 Z" fill="#4d5358"/>
    <path d="M0 740 C180 720 420 718 620 732 C760 742 880 722 1000 700 L1000 722 C880 746 760 766 620 756 C420 742 200 746 0 766 Z" fill="#ee7a2a"/>
    <path d="M0 250 C80 250 140 280 170 320 L0 320 Z" fill="#ee7a2a"/>
    <circle cx="700" cy="300" r="272" fill="none" stroke="#ee7a2a" stroke-width="14" stroke-dasharray="860 900" transform="rotate(120 700 300)"/>
    <circle cx="700" cy="300" r="296" fill="none" stroke="#c9cdd0" stroke-width="6" stroke-dasharray="520 1400" transform="rotate(-40 700 300)"/>
  </svg>

  <div class="brand"><span class="brand__mark"></span><span class="brand__name">Durable Residence Backers League</span></div>

  <div class="photo" role="img" aria-label="Photo of a hand stacking coins beside a small model house" style="left:450px;top:50px;width:500px;height:500px"></div>

  <div class="headline">
    <div class="headline__lead">Where LIHTC</div>
    <div class="headline__tag">Investing Excellence Begins</div>
    <div class="headline__sub">The Only Community Built Exclusively for Investors</div>
  </div>

  <p class="intro"><strong>DRBL is where federal housing credit investors</strong> — banks, insurers and economic investors — meet, learn and lead. We are the only organization solely dedicated to credit investors, giving you a trusted peer network, shared market insight and a voice in shaping industry standards.</p>

  <div class="stats">
    <div class="stat"><b>30</b> YEARS OF IMPACT</div>
    <div class="stat"><b>63+</b> INVESTOR FIRMS</div>
    <div class="stat"><b>1,000+</b> INDUSTRY PROFESSIONALS</div>
  </div>

  <div class="activities">
    <div class="activities__title">What Members Do</div>
    <ul>
      <li><b>Network:</b> Peer Groups &amp; Forums</li>
      <li><b>Learn:</b> Conferences &amp; Webinars</li>
      <li><b>Share:</b> Candid Investor Exchange</li>
      <li><b>Shape:</b> Standards &amp; Best Practices</li>
      <li><b>Grow:</b> Professional Development</li>
    </ul>
  </div>

  <p class="access">Firm membership, unmatched access.<br>Your entire team can participate in DRBL activities.</p>

  <div class="join">
    <span class="join__tab">Join DRBL Today</span>
    <div class="join__grid">
      <div class="tier">
        <div class="tier__name">Investor Members</div>
        Banks, Insurance Companies, Economic Investors<br>
        <span class="tier__price">$5,890/year</span> (assets &gt;$1B)<br>
        <span class="tier__price">$1,000/year</span> (assets &lt;$1B)
      </div>
      <div class="tier">
        <div class="tier__name">Affiliate Members</div>
        Syndicators &amp; Brokers<br>
        <span class="tier__price">$4,540/year</span>
      </div>
    </div>
  </div>

  <div class="footer"><span class="footer__cta">Ready to join?</span><span class="footer__url">drbl.org</span></div>
</section>

<section class="page page--back">
  <div class="brand"><span class="brand__mark"></span><span class="brand__name">Durable Residence Backers League</span></div>

  <div class="benefits-panel"></div>
  <div class="benefits-hero"><h1>Member<br>Benefits</h1></div>
  <div class="feature-panel">
    <div class="feature">
      <h2>Members-Only Conferences</h2>
      <p>Two annual in-person meetings, Spring Meeting and Fall Forum, for candid peer conversations, expert panels and valuable networking with syndicators and lenders.</p>
    </div>
    <div class="feature">
      <h2>Investor-Only Forums</h2>
      <p>Exclusive meetings and webinars for investor-only members to discuss market conditions, underwriting and meaningful collaboration.</p>
    </div>
  </div>

  <div class="perks">
    <div class="perk"><h3>Searchable Member Directory</h3><p>Find underwriters, asset managers and credit officers across member firms by name, role and region.</p></div>
    <div class="perk"><h3>Shape Industry Standards <span>[INVESTOR ONLY]</span></h3><p>DRBL's underwriting and asset management standards are adopted industry-wide and reflect member expertise.</p></div>
    <div class="perk"><h3>Emerging Leaders Program <span>[INVESTOR ONLY]</span></h3><p>Develop your firm's next generation of leaders through dedicated mentoring and professional development programs.</p></div>
  </div>

  <div class="side-card">
    <div class="perk"><h3>Peer-to-Peer Meetups</h3><p>Find your peer underwriters, asset managers and credit officers in small-group meetups.</p></div>
    <div class="perk"><h3>Live &amp; On-Demand Webinars</h3><p>Monthly Third Thursday webinars covering credit market trends, tax reform, asset management and current industry topics.</p></div>
  </div>

  <div class="firms">Harbor Mutual Life • Crestline Bank • Northgate Trust • Willow Federal • Summit Ridge Bank • Lakeview Financial • Granite Capital • Pinecrest Insurance • Meridian Savings • Oakhurst Bancorp • Bluewater Trust • Redstone Mutual • Cedar Valley Bank • Fairhaven Capital • Ironwood Financial • Silverline Bank • Brookfield Savings • Stonebridge Insurance • Westmark Trust • Hollis Bancshares</div>

  <div class="footer"><span class="footer__cta">Ready to join?</span><span class="footer__url">drbl.org</span></div>
</section>

</body>
</html>
```